Redesign Of Flower Delivery Subscription Service Website

I need a revamped website of www.petal-rush.com

Please revamp current design using same content....

Target Market(s)

people who buy flowers. Brides, wedding planners, wedding photographer, married man, boyfriend, etc.

Industry/Entity Type

Florist

Number of Pages Required

5+ page

Colors

Designer to choose colors to be used in the design.

Requirements
Must have
• I need a revamped website of www.petal-rush.com
• Please revamp current design using same content....
Nice to have
Should not have

```html
<!DOCTYPE html>
<html lang="en">
<head>
<meta charset="utf-8">
<title>Petal Rush – Monthly Flower Delivery</title>
<link href="https://fonts.googleapis.com/css2?family=Questrial&family=Montserrat:wght@600;700&family=Open+Sans:wght@400;600;700&display=swap" rel="stylesheet">
<style>
  :root{
    --hero-pink:#f6d3d3;
    --band-pink:#e59c94;
    --leaf-grey:#ececec;
    --ink:#333333;
    --muted:#666666;
    --green:#8cc63f;
    --blue:#2b9fd9;
    --white:#ffffff;
    --line:#e4e4e4;
  }
  *{box-sizing:border-box;margin:0;padding:0}
  html,body{width:1200px;height:2733px;overflow:hidden;background:var(--white)}
  body{position:relative;font-family:"Open Sans",Arial,sans-serif;color:var(--ink)}
  .abs{position:absolute}

  /* brand */
  .brand{text-align:center;font-family:"Questrial",sans-serif;color:var(--green);white-space:nowrap}
  .brand__name{display:block;font-size:42px;line-height:1;letter-spacing:1px;white-space:nowrap}
  .brand__tag{display:block;font-family:"Open Sans",sans-serif;font-size:10px;color:var(--muted);margin-top:4px;letter-spacing:.5px;white-space:nowrap}

  /* hero */
  .hero{left:0;top:0;width:1200px;height:601px;background:var(--hero-pink)}
  .hero .brand{left:465px;top:38px;width:270px}
  .hero__title{left:0;top:150px;width:1200px;text-align:center;font-family:"Questrial",sans-serif;font-size:88px;color:#3b3b3b;letter-spacing:1px}
  .hero__sub{left:0;top:262px;width:1200px;text-align:center;font-size:14px;color:var(--ink)}
  .hero__price{left:0;top:290px;width:1200px;text-align:center;font-size:13px;color:var(--ink)}
  .hero__price strong{color:#d9534f;font-weight:700}
  .hero__flowers{left:0;top:350px;width:1200px;height:251px;background:linear-gradient(180deg,rgba(246,211,211,0) 0%,#f2b8b8 30%,#f4c9b8 60%,#e9a7a7 100%)}

  /* nav */
  .nav{left:0;top:601px;width:1200px;height:69px;background:var(--white);box-shadow:0 2px 6px rgba(0,0,0,.08)}
  .nav .brand{left:160px;top:14px;width:190px;text-align:left}
  .nav .brand__name{font-size:28px}
  .nav .brand__tag{font-size:8px;margin-top:2px}
  .nav__links{left:372px;top:28px;display:flex;gap:20px;list-style:none;font-size:10px;font-weight:600;text-transform:uppercase;color:var(--ink);white-space:nowrap}
  .nav__links .is-active{color:var(--green)}
  .nav__buy{left:988px;top:601px;width:52px;height:68px}

  /* soft leaf background */
  .leaf-bg{background:var(--leaf-grey)}

  /* how it works */
  .how{left:0;top:670px;width:1200px;height:700px}
  .how__card{left:410px;top:716px;width:383px;height:528px;background:var(--white);box-shadow:0 3px 14px rgba(0,0,0,.12);text-align:center}
  .how__title{margin-top:42px;display:flex;align-items:center;justify-content:center;gap:12px;font-family:"Montserrat",sans-serif;font-weight:700;font-size:24px;color:var(--ink)}
  .how__title::before,.how__title::after{content:"";width:58px;height:2px;background:var(--ink)}
  .how__lead{margin-top:20px;font-size:14px;font-weight:700;font-style:italic;color:var(--blue)}
  .how__text{margin:16px 34px 0;font-size:11.5px;line-height:1.6;color:var(--muted)}
  .how__more{display:inline-block;margin-top:14px;font-size:12px;font-weight:700;color:var(--ink)}
  .how__video{position:absolute;left:0;top:290px;width:383px;height:238px;background:linear-gradient(135deg,#5a5a5a,#bdbdbd 55%,#8a8a8a)}

  /* pink wave band */
  .band{left:0;top:1300px;width:1200px;height:530px}
  .band svg{display:block}
  .feature{top:1400px;width:268px;text-align:center}
  .feature__photo{height:245px;border:6px solid var(--white);box-shadow:0 3px 10px rgba(0,0,0,.15)}
  .feature__title{margin-top:28px;font-family:"Montserrat",sans-serif;font-weight:600;font-size:17px;color:var(--white)}
  .feature__text{margin-top:8px;font-size:10.5px;line-height:1.45;color:var(--white);font-weight:600}
  .dots{left:580px;top:1750px;display:flex;gap:6px}
  .dots span{width:10px;height:4px;background:rgba(255,255,255,.55);border-radius:2px}
  .dots span.is-on{background:var(--white)}

  /* monthly subscription */
  .subscribe{left:0;top:1830px;width:1200px;height:660px}
  .subscribe__panel{left:159px;top:1886px;width:880px;height:560px;background:var(--white);box-shadow:0 3px 14px rgba(0,0,0,.1)}
  .subscribe__title{margin-top:78px;text-align:center;font-family:"Montserrat",sans-serif;font-weight:700;font-size:27px;line-height:1.35;color:#222}
  .subscribe__text{margin:26px 40px 0;text-align:center;font-size:11.5px;line-height:1.65;color:var(--muted)}
  .offers{position:absolute;left:12px;top:280px;display:flex;gap:28px}
  .offer{width:260px;height:240px;background:#f4f4f4;padding:8px}
  .offer__inner{height:100%;background:var(--white);text-align:center;padding:16px 18px 0}
  .offer__title{font-family:"Montserrat",sans-serif;font-weight:700;font-size:16px;color:#222}
  .offer__text{margin-top:10px;font-size:10.5px;line-height:1.55;color:var(--muted);height:110px;overflow:hidden}
  .offer__btn{display:inline-block;margin-top:16px;width:100px;padding:8px 0;background:var(--green);color:var(--white);font-size:12px;font-weight:600}

  /* footer */
  .footer{left:0;top:2490px;width:1200px;height:243px;background:var(--white)}
  .footer-brand{left:160px;top:2560px;width:260px;text-align:left}
  .footer-brand .brand__name{font-size:40px}
  .footer__contact{left:502px;top:2575px;font-size:10.5px;line-height:1.9;color:var(--muted);font-style:normal}
  .footer__contact strong{display:block;color:var(--ink);font-size:11px}
  .footer__legal{left:839px;top:2575px;font-size:10px;line-height:1.7;color:var(--muted)}
</style>
</head>
<body>

<header class="hero abs">
  <div class="brand abs"><span class="brand__name">Petal Rush</span><span class="brand__tag">San Diego Flower Company</span></div>
  <h1 class="hero__title abs">ALWAYS FRESH</h1>
  <p class="hero__sub abs">Beautiful Flower Arrangements Delivered Monthly</p>
  <p class="hero__price abs">Now only <strong>$69.95/MTH ($100 value)</strong></p>
  <div class="hero__flowers abs" role="img" aria-label="Row of pink and cream lisianthus flowers on a pink background"></div>
</header>

<nav class="nav abs">
  <div class="brand abs"><span class="brand__name">Petal Rush</span><span class="brand__tag">San Diego Flower Company</span></div>
  <ul class="nav__links abs">
    <li class="is-active">Home</li><li>How it works</li><li>Delivery Areas</li><li>Franchise</li><li>My Account</li><li>Blog</li><li>Free Flowers Monthly</li>
  </ul>
</nav>
<svg class="nav__buy abs" viewBox="0 0 52 68" aria-label="Buy Now">
  <path d="M0 0H52V68L26 58L0 68Z" fill="#5aaee6"/>
  <text x="26" y="28" text-anchor="middle" font-family="Open Sans, sans-serif" font-size="10" font-weight="700" fill="#fff">Buy</text>
  <text x="26" y="42" text-anchor="middle" font-family="Open Sans, sans-serif" font-size="10" font-weight="700" fill="#fff">Now</text>
</svg>

<section class="how abs leaf-bg" role="img" aria-label="Soft grey background of scattered roses and leaves"></section>
<article class="how__card abs">
  <h2 class="how__title">How It Works</h2>
  <p class="how__lead">Petal Rush is a "SET IT and FORGET IT"</p>
  <p class="how__text">subscription based flower delivery service. For an amazing price Petal Rush will hand deliver a gorgeous arrangement directly to anyone, anywhere you want, every month! When setting up your account, Petal Rush even lets you choose exact delivery dates for your Anniversary, Birthday, Valentine's and Mother's Day.</p>
  <span class="how__more">Read More →</span>
  <div class="how__video" role="img" aria-label="Video still of a hand sketching a flower delivery illustration"></div>
</article>

<section class="band abs">
  <svg width="1200" height="530" viewBox="0 0 1200 530" aria-hidden="true">
    <path d="M0 40 C200 -10 380 70 600 30 C820 -10 1000 60 1200 20 V500 C1000 540 820 470 600 510 C380 550 200 470 0 510Z" fill="#e59c94"/>
  </svg>
</section>
<div class="feature abs" style="left:159px">
  <div class="feature__photo" role="img" aria-label="Bouquet of purple and violet roses in a vase" style="background:linear-gradient(160deg,#dfe9d6,#7a3f7a 55%,#4f6b3a)"></div>
  <h3 class="feature__title">Set it and forget it</h3>
  <p class="feature__text">Petal Rush is a "SET IT and FORGET IT" subscription based flower delivery service.</p>
</div>
<div class="feature abs" style="left:466px">
  <div class="feature__photo" role="img" aria-label="Arrangement of cream and blush roses" style="background:linear-gradient(160deg,#f7f2ea,#ecd9c4 55%,#c9a98c)"></div>
  <h3 class="feature__title">But never forget again</h3>
  <p class="feature__text">When setting up your account, you can choose exact delivery dates for the months that matter.</p>
</div>
<div class="feature abs" style="left:772px">
  <div class="feature__photo" role="img" aria-label="Bouquet of coral pink roses with greenery" style="background:linear-gradient(160deg,#f6eeee,#e7857f 55%,#6f8f4f)"></div>
  <h3 class="feature__title">Making Someone's day</h3>
  <p class="feature__text">Be the hero in that special someone's life each and every month.</p>
</div>
<div class="dots abs"><span></span><span class="is-on"></span><span></span></div>

<section class="subscribe abs leaf-bg" role="img" aria-label="Soft grey background of scattered roses and leaves"></section>
<article class="subscribe__panel abs">
  <h2 class="subscribe__title">Monthly Subscription Based Flower Delivery Service<br>in San Diego CA by Our Florist Shop</h2>
  <p class="subscribe__text">Every moment of life could be cherished perfectly ... if you choose wisely. To make your day more treasured, remember that flowers are the smartest choice when delivered through our monthly Petal Rush subscription based delivery service. Our online subscription based flower delivery service can help you pamper, cherish and make an everlasting impression on the minds of your loved ones with a doorstep delivery of exquisitely hand-designed floral arrangements.</p>
  <div class="offers">
    <div class="offer"><div class="offer__inner">
      <h3 class="offer__title">Set it and forget it</h3>
      <p class="offer__text">Let's not forget a single day in which you can make your loved ones feel special. Whether it's your anniversary or a birthday in your family, you must always go an extra mile to show...</p>
      <span class="offer__btn">More</span>
    </div></div>
    <div class="offer"><div class="offer__inner">
      <h3 class="offer__title">Standord And Persona</h3>
      <p class="offer__text">Send Flower Arrangements For Special Occasions Petal Rush offers online subscription based service that is hassle free, trustable and affordable at the same time. We offer the most trusted and</p>
      <span class="offer__btn">More</span>
    </div></div>
    <div class="offer"><div class="offer__inner">
      <h3 class="offer__title">Get Yourself Subscribed</h3>
      <p class="offer__text">And Claim Discounts On Big Orders! Get love and adulation by gifting flowers to your loved ones on those special occasions. Whether it's formal, personal or your time for your family, just follow the</p>
      <span class="offer__btn">More</span>
    </div></div>
  </div>
</article>

<footer class="footer abs"></footer>
<div class="brand footer-brand abs"><span class="brand__name">Petal Rush</span><span class="brand__tag">San Diego Flower Company</span></div>
<address class="footer__contact abs">
  <strong>PETAL RUSH</strong>
  EMAIL : info@petal-rush.com<br>
  TEL : 555-0148<br>
  FAX : 555-0172
</address>
<p class="footer__legal abs">© Copyright 2016 Petal Rush. All rights reserved.<br>Privacy Policy<br>Terms And Conditions</p>

</body>
</html>
```